Kit Layout de Posts para Redes Sociais (Facebook, Instagram e etc)para Dra Marcela Toledano
Postado por: marcelatoledano_5830174416   Estou Offline
Projeto para criar:
Kit Layout de Posts para Redes Sociais (Facebook, Instagram e etc)
Clientes com PC preferem arquivos em CorelDraw (CDR).
Imagem: Imagem JPG (alta resoluçao) PNG em camadas PSD em camadas PDF Sem Preferência Tipos possíveis: Imagem JPG (alta resoluçao), PNG em camadas, PSD em camadas, PDF.

```html
<!DOCTYPE html>
<html lang="pt-BR">
<head>
<meta charset="utf-8">
<title>Post — Dra. Marcela Toledano</title>
<link href="https://fonts.googleapis.com/css2?family=Raleway:wght@200;300;400&display=swap" rel="stylesheet">
<style>
  :root {
    --plum: #6e4a61;
    --plum-deep: #5d3c52;
    --gold: #c9a46c;
    --gold-light: #e2c99a;
    --paper: #ffffff;
    --mist: #f4f1f2;
    --skin-light: #f3ddd2;
    --skin-mid: #e4bfae;
    --hair: #b59a77;
    --white: #ffffff;
  }
  * { margin: 0; padding: 0; box-sizing: border-box; }
  html, body { width: 1200px; height: 1200px; overflow: hidden; background: var(--paper); }
  .post {
    position: relative;
    width: 1200px;
    height: 1200px;
    overflow: hidden;
    background: linear-gradient(90deg, var(--paper) 0%, var(--mist) 100%);
    font-family: "Raleway", sans-serif;
  }
  .portrait {
    position: absolute;
    left: 430px;
    top: 0;
    width: 770px;
    height: 1000px;
    background:
      radial-gradient(ellipse 46% 36% at 58% 8%, var(--hair) 0%, rgba(181,154,119,0) 100%),
      radial-gradient(ellipse 44% 52% at 56% 48%, var(--skin-light) 0%, var(--skin-mid) 60%, rgba(228,191,174,0) 100%),
      radial-gradient(ellipse 40% 30% at 50% 92%, var(--skin-mid) 0%, rgba(228,191,174,0) 100%);
    -webkit-mask-image: linear-gradient(90deg, transparent 0%, #000 22%);
            mask-image: linear-gradient(90deg, transparent 0%, #000 22%);
  }
  .headline {
    position: absolute;
    left: 66px;
    top: 150px;
    color: var(--plum);
    font-weight: 300;
    line-height: 1;
    text-transform: uppercase;
  }
  .headline__accent {
    position: absolute;
    left: -40px;
    top: 28px;
    width: 10px;
    height: 230px;
    background: linear-gradient(180deg, var(--gold-light), var(--gold));
  }
  .headline__small { display: block; font-size: 112px; letter-spacing: 2px; }
  .headline__large { display: block; font-size: 172px; letter-spacing: 4px; margin-top: 4px; }
  .footer-band {
    position: absolute;
    left: 0;
    top: 860px;
    width: 1200px;
    height: 340px;
  }
  .brand {
    position: absolute;
    left: 66px;
    top: 1045px;
    display: flex;
    align-items: center;
    gap: 22px;
  }
  .brand__dot {
    width: 78px;
    height: 78px;
    border-radius: 50%;
    border: 3px solid var(--gold-light);
  }
  .brand__name {
    color: var(--gold-light);
    font-weight: 300;
    font-size: 44px;
    line-height: 1.1;
    letter-spacing: 1px;
  }
  .divider {
    position: absolute;
    left: 628px;
    top: 1050px;
    width: 2px;
    height: 130px;
    background: rgba(255,255,255,0.35);
  }
  .contacts {
    position: absolute;
    left: 766px;
    top: 1058px;
    list-style: none;
    color: var(--white);
    font-weight: 400;
    font-size: 26px;
  }
  .contacts__item { display: flex; align-items: center; gap: 14px; height: 52px; }
  .contacts__icon {
    width: 32px; height: 32px; border-radius: 50%;
    background: var(--gold);
    display: flex; align-items: center; justify-content: center;
  }
</style>
</head>
<body>
  <main class="post">
    <div class="portrait" role="img" aria-label="Fotografia de uma mulher com marcações de procedimento estético no rosto e mãos com luvas azuis"></div>

    <h1 class="headline">
      <span class="headline__accent"></span>
      <span class="headline__small">Seu texto</span>
      <span class="headline__large">Aqui</span>
    </h1>

    <svg class="footer-band" viewBox="0 0 1200 340" preserveAspectRatio="none" aria-hidden="true">
      <path d="M0 20 C 320 0, 700 40, 1200 112" fill="none" stroke="var(--gold)" stroke-width="5"/>
      <path d="M0 30 C 320 12, 700 52, 1200 126 L1200 340 L0 340 Z" fill="var(--plum)"/>
    </svg>

    <div class="brand">
      <span class="brand__dot"></span>
      <p class="brand__name">Dra. Marcela<br>Toledano</p>
    </div>

    <span class="divider"></span>

    <ul class="contacts">
      <li class="contacts__item">
        <span class="contacts__icon">
          <svg width="18" height="18" viewBox="0 0 24 24" aria-hidden="true"><path fill="var(--white)" d="M6.6 10.8a15.1 15.1 0 0 0 6.6 6.6l2.2-2.2c.3-.3.7-.4 1-.2 1.1.4 2.3.6 3.6.6.6 0 1 .4 1 1V20c0 .6-.4 1-1 1A17 17 0 0 1 3 4c0-.6.4-1 1-1h3.5c.6 0 1 .4 1 1 0 1.3.2 2.5.6 3.6.1.3 0 .7-.2 1z"/></svg>
        </span>
        (00) 4817-3926
      </li>
      <li class="contacts__item">
        <span class="contacts__icon"></span>
        @DraMarcelaToledano
      </li>
    </ul>
  </main>
</body>
</html>
```